Bright Horizon Painting and Remodeling needs a business card

Business card should have company logo. I will upload two different logos and let me see which one is a better design for the business card.

Name of company: Bright Horizon Painting and Remodeling
Address: 4126 NW 71st st Suite 214
Miami, FL 33166

local phone: (305) 555-0142
toll free (855) 555-0197
fax (866) 555-0163

email: corinne@paintingbrighthorizon.example

not sure if i should include social media links or names on the business card.

company does interior and exterior painting, pressure washing, wall paper removal, drywall and stucco repair, staining,

We give free estimates.

I want a two sided business card.

Not sure if all this information is necessary for the business card. Designer can pick out whatever information they deem is important for a consumer to see on the business card.

Anticipating on the business card to be printed on nice quality.

I will upload an image of one of the logos on a type of business card surface. That idea can be used as well. Be creative. Business card should be professional but very nice and eye catching.

remove drywall and stucco repair and replace with tile installation

Industry/Entity Type

Business

Contact Information for Business Card

Miami, FL 33166

toll free (855) 555-0197
fax (866) 555-0163

company does interior and exterior painting, pressure washing, wall paper removal, drywall and stucco repair, staining, tile removal, *specializing in vinyl floor removal

free estimates.

Requirements
Must have
• Profesional font

```html
<!DOCTYPE html>
<html lang="en">
<head>
<meta charset="utf-8">
<title>Bright Horizon Painting and Remodeling – Business Card</title>
<link rel="stylesheet" href="https://fonts.googleapis.com/css2?family=Saira+Extra+Condensed:wght@700&family=Saira+Condensed:wght@400&display=swap">
<style>
  :root {
    --paper: #ffffff;
    --ink: #111111;
    --brand-green: #5db088;
    --band-grey: #e0e0e0;
    --sweep-purple: #9a72b6;
    --sweep-teal: #86a8a6;
    --sweep-green: #7dc896;
    --sweep-tan: #c9a97a;
    --sweep-orange: #f48a5e;
    --sweep-coral: #ef6f52;
  }
  html, body {
    margin: 0;
    padding: 0;
    width: 1200px;
    height: 769px;
    overflow: hidden;
    background: var(--paper);
  }
  .card {
    display: block;
    width: 1200px;
    height: 769px;
  }
  .brand-name {
    font-family: "Saira Extra Condensed", "Arial Narrow", sans-serif;
    font-weight: 700;
    font-size: 80px;
    fill: var(--ink);
  }
  .contact-line {
    font-family: "Saira Condensed", "Arial Narrow", sans-serif;
    font-weight: 400;
    font-size: 35px;
    fill: var(--ink);
  }
</style>
</head>
<body>
<svg class="card" viewBox="0 0 1200 769" xmlns="http://www.w3.org/2000/svg" role="img" aria-label="Bright Horizon Painting and Remodeling business card">
  <defs>
    <linearGradient id="sweep-gradient" x1="0" y1="0" x2="1" y2="0">
      <stop offset="0" stop-color="var(--sweep-purple)"/>
      <stop offset="0.15" stop-color="var(--sweep-teal)"/>
      <stop offset="0.3" stop-color="var(--sweep-green)"/>
      <stop offset="0.5" stop-color="var(--sweep-tan)"/>
      <stop offset="0.68" stop-color="var(--sweep-orange)"/>
      <stop offset="1" stop-color="var(--sweep-coral)"/>
    </linearGradient>
  </defs>

  <g class="title-banner">
    <polygon class="banner-grey" points="466,149 1200,149 1200,240 442,240" fill="var(--band-grey)"/>
    <polygon class="banner-green" points="0,142 459,142 427,247 0,247" fill="var(--brand-green)"/>
    <text class="brand-name" x="80" y="226" textLength="340" lengthAdjust="spacingAndGlyphs">Bright Horizon</text>
    <text class="brand-name" x="474" y="226" textLength="654" lengthAdjust="spacingAndGlyphs">Painting and Remodeling</text>
  </g>

  <g class="contact-block">
    <text class="contact-line" x="479" y="338">4126 NW 71st st Suite 214, Miami, FL 33166</text>
    <text class="contact-line" x="479" y="440">Local Phone (305) 555-0142</text>
    <text class="contact-line" x="479" y="492">Toll Free (855) 555-0197</text>
    <text class="contact-line" x="479" y="544">Fax (866) 555-0163</text>
    <text class="contact-line" x="479" y="650">corinne@paintingbrighthorizon.example</text>
  </g>

  <path class="colour-sweep" d="M0,747 Q600,735 1200,714 L1200,769 L0,769 Z" fill="url(#sweep-gradient)"/>
</svg>
</body>
</html>
```